New to ArtHarbor? This Contest is for you!

Are you new to ArtHarbor and looking to enter your first contest? Look no further! We're launching this special contest to help you get started on building a design portfolio at ArtHarbor!

Requirements:
* Create a beautiful and eye-catching graphic design which includes the words "Spot me at ArtHarbor!"
* Upload your design to this contest AND share it on Chatterly
* You must upload your entry before 12:00am 1 April
* This must be your very FIRST entry on ArtHarbor to be eligible to receive a prize. If you've already entered other ArtHarbor contests you won't be eligible to win the prizes
* Your design must adhere to our quality standards to be eligible to receive a prize

Prizes:
* There are 150 x $5 participation payments ($750) available to be awarded to high-quality designs
* First prize for the best design is $150
* Second prize is $100

Requirements
Must have
• Your design must contain the words "Spot me at ArtHarbor".
• This must be your first entry on ArtHarbor to be eligible for the prizes.
• Your design must adhere to our quality standards.
Should not have
• No stock images or overused concepts.

```html
<!DOCTYPE html>
<html lang="en">
<head>
<meta charset="utf-8">
<title>Spot me at ArtHarbor</title>
<link rel="stylesheet" href="https://fonts.googleapis.com/css2?family=League+Gothic&family=Playfair+Display:ital,wght@1,400;1,900&display=swap">
<style>
  :root {
    --sky: #41abe2;
    --ink: #0a0a0a;
    --muted: #3a3a3a;
    --white: #ffffff;
    --pale: #e6f1fb;
    --amp: #a8d2f2;
    --leaf: #5dbb46;
    --badge: #4caf3e;
    --figure-top: #4a4f55;
    --figure-bottom: #2f3337;
    --band-a: #f4c21a;
    --band-b: #8cc63f;
  }
  html, body {
    margin: 0;
    padding: 0;
    width: 1200px;
    height: 676px;
    overflow: hidden;
    background: var(--sky);
  }
  .poster {
    display: block;
    width: 1200px;
    height: 676px;
  }
  .condensed { font-family: "League Gothic", "Oswald", sans-serif; }
  .serif-italic { font-family: "Playfair Display", Georgia, serif; font-style: italic; }
  .count { font-weight: 900; fill: var(--pale); stroke: #1d2b38; stroke-width: 1.5; }
  .count-label { fill: var(--leaf); }
  .headline { fill: var(--ink); }
  .aside { fill: var(--muted); }
  .ampersand { font-weight: 400; fill: var(--amp); stroke: #2c4f6b; stroke-width: 1.2; }
  .guarantee { fill: var(--white); }
  .guarantee-note { fill: #1e2a33; }
  .invite { font-weight: 900; fill: var(--white); }
  .badge-line { fill: var(--ink); }
</style>
</head>
<body>
<svg class="poster" viewBox="0 0 1200 676" xmlns="http://www.w3.org/2000/svg">
  <defs>
    <linearGradient id="figureTone" x1="0" y1="0" x2="0" y2="1">
      <stop offset="0" stop-color="var(--figure-top)"/>
      <stop offset="1" stop-color="var(--figure-bottom)"/>
    </linearGradient>
    <linearGradient id="bandTone" x1="0" y1="0" x2="1" y2="0">
      <stop offset="0" stop-color="var(--band-a)"/>
      <stop offset="0.5" stop-color="var(--band-b)"/>
      <stop offset="1" stop-color="var(--band-a)"/>
    </linearGradient>
  </defs>

  <rect class="backdrop" width="1200" height="676" fill="var(--sky)"/>

  <rect class="figure" x="222" y="0" width="222" height="676" rx="90" fill="url(#figureTone)"
        role="img" aria-label="Silhouette of a standing woman filled with a grey swirl pattern"/>

  <text class="count serif-italic" x="50" y="270" font-size="190" textLength="272" lengthAdjust="spacingAndGlyphs">40</text>
  <text class="count-label condensed" x="287" y="334" font-size="36">Categories</text>

  <text class="headline condensed" x="596" y="222" font-size="112" textLength="346" lengthAdjust="spacingAndGlyphs">Quick and Easy</text>
  <text class="aside condensed" x="944" y="218" font-size="24">to get started</text>

  <text class="aside condensed" x="594" y="313" font-size="24">you set</text>
  <text class="headline condensed" x="650" y="313" font-size="112" textLength="400" lengthAdjust="spacingAndGlyphs">Your Own Budget</text>
  <text class="aside condensed" x="1051" y="313" font-size="24">and your terms</text>

  <text class="headline condensed" x="596" y="404" font-size="112" textLength="394" lengthAdjust="spacingAndGlyphs">25 to 100+ Ideas</text>
  <text class="aside condensed" x="992" y="404" font-size="24">per project</text>

  <text class="ampersand serif-italic" x="498" y="566" font-size="200">&amp;</text>

  <text class="guarantee condensed" x="655" y="587" font-size="98" textLength="120" lengthAdjust="spacingAndGlyphs">100%</text>
  <text class="guarantee-note condensed" x="793" y="585" font-size="28">Money Back</text>
  <text class="guarantee condensed" x="897" y="587" font-size="112" textLength="250" lengthAdjust="spacingAndGlyphs">Guarantee!</text>
  <text class="guarantee-note condensed" x="1150" y="572" font-size="22">*</text>

  <text class="invite serif-italic" x="89" y="505" font-size="50" textLength="309" lengthAdjust="spacingAndGlyphs">Interested?</text>

  <g class="badge">
    <circle cx="263" cy="580" r="80" fill="var(--badge)" stroke="#1a1a1a" stroke-width="1.5"/>
    <text class="badge-line condensed" x="263" y="568" font-size="32" text-anchor="middle">Spot me at</text>
    <text class="badge-line condensed" x="263" y="607" font-size="40" text-anchor="middle">ArtHarbor</text>
  </g>

  <rect class="floral-band" x="0" y="651" width="1200" height="14" fill="url(#bandTone)"
        role="img" aria-label="Decorative strip of yellow and green flowers"/>
</svg>
</body>
</html>
```